Logo and Packaging Design for Apparel and Textiles Business

Hi,

Our Business:
We are an apparel and home textiles business and would like to have a logo designed for our business as well as packaging for our products.

Products:
Initially, we are only selling Bed Sheet sets/ Towel sets and also women stoles, however later on will be expanding into apparel i.e. T-Shirts and Jeans and other clothing. Hence, packaging design should be generic enough that all of the above items can relate to it , yet it should be unique enough to leave a distinctive mark.

Design Preferences:
you can visit our website at lumbrova.com.au, we have just put up the website template but have not updated it with our custom content, hence all the write-up is in Latin. However, visiting the website should give you a good idea of the color schemes to use both in Logo as well as the packaging design. The logo will be displayed on the website and hence will need to fall into contrast with existing website layout/colors. Please note the packaging design will be used to create card board packaging for all of the above products.

Business Name To be Highlighted:
Please note that business name that should be highlighted in the design for both logo and packaging is "Lumbrova". If it matters in coming up with a design, the word "lumbrova" is a combo of two words "thread" and "unique".

Industry/Entity Type

Business

Logo Text

'weaving excellence'.... or 'the woven elegance'

```html
<!DOCTYPE html>
<html lang="en">
<head>
<meta charset="utf-8">
<title>Lumbrova Pack Proposal</title>
<link rel="stylesheet" href="https://fonts.googleapis.com/css2?family=Pacifico&family=Playfair+Display:wght@700&family=Montserrat:wght@300&display=swap">
<style>
  :root {
    --paper: #ffffff;
    --pack-yellow: #fdc82f;
    --stitch-green: #8cc152;
    --edge-olive: #8a7d3a;
    --rule-grey: #8d8a80;
    --brand-red: #c8382c;
    --script-ink: #111111;
    --photo-frame: #fde79a;
    --note-ink: #6c6c6c;
    --footer-blue: #a9c4d2;
    --caption-ink: #7d8a90;
    --squiggle: #a9d46a;
  }
  html, body {
    margin: 0;
    padding: 0;
    width: 1200px;
    height: 849px;
    overflow: hidden;
    background: var(--paper);
  }
  .sheet {
    position: relative;
    width: 1200px;
    height: 849px;
  }
  .sheet svg { display: block; }
  .pack-shape { fill: var(--pack-yellow); stroke: var(--edge-olive); stroke-width: 1; }
  .pack-stitch { fill: none; stroke: var(--stitch-green); stroke-width: 3; stroke-dasharray: 2 4; }
  .pack-rule { stroke: var(--rule-grey); stroke-width: 1; }
  .pack-squiggle { fill: none; stroke: var(--squiggle); stroke-width: 1.4; }
  .brand-name {
    font-family: "Playfair Display", Georgia, serif;
    font-weight: 700;
    fill: var(--brand-red);
  }
  .maker-script {
    font-family: "Pacifico", cursive;
    fill: var(--script-ink);
  }
  .photo-frame { fill: none; stroke: var(--photo-frame); stroke-width: 3; }
  .photo-slot-outline { fill: none; stroke: var(--paper); stroke-width: 0.8; }
  .note-line { fill: none; stroke: #333333; stroke-width: 0.8; }
  .note-text {
    font-family: "Montserrat", Arial, sans-serif;
    font-weight: 300;
    font-size: 11px;
    letter-spacing: 6px;
    fill: var(--note-ink);
  }
  .footer-rule { stroke: var(--footer-blue); stroke-width: 4; }
  .footer-caption {
    font-family: "Montserrat", Arial, sans-serif;
    font-weight: 300;
    font-size: 12px;
    letter-spacing: 6px;
    fill: var(--caption-ink);
  }
</style>
</head>
<body>
<div class="sheet">
  <svg width="1200" height="849" viewBox="0 0 1200 849" xmlns="http://www.w3.org/2000/svg">
    <defs>
      <linearGradient id="bedroom-tones" x1="0" y1="0" x2="0" y2="1">
        <stop offset="0" stop-color="#d9d6d2"/>
        <stop offset="0.5" stop-color="#e8e6e3"/>
        <stop offset="0.72" stop-color="#6f86a8"/>
        <stop offset="1" stop-color="#2f4f7f"/>
      </linearGradient>
      <g id="pack-panel">
        <path class="pack-shape" d="M93,367 C250,356 330,305 430,250 C560,182 650,124 800,117 L800,617 L93,617 Z"/>
        <path class="pack-stitch" d="M96,370 C252,359 332,308 432,253 C561,186 651,127 797,120 L797,614 M96,370 L96,614"/>
        <line class="pack-rule" x1="93" y1="507" x2="800" y2="507"/>
        <line class="pack-rule" x1="93" y1="549" x2="800" y2="549"/>
        <path class="pack-squiggle" d="M100,495 C160,470 230,500 300,478 C400,450 500,470 600,468 C680,466 740,480 760,500 C780,520 700,545 640,525 C610,515 600,560 650,580 C700,595 760,560 790,540"/>
        <path class="pack-squiggle" d="M340,548 C380,520 430,560 480,545 C520,532 560,560 600,550"/>
        <text class="brand-name" x="135" y="468" font-size="82" textLength="635" lengthAdjust="spacing">LUMBROVA</text>
        <text class="maker-script" x="568" y="258" font-size="28">Loomhaven</text>
        <text class="maker-script" x="115" y="540" font-size="28">Loomhaven</text>
        <text class="brand-name" x="360" y="542" font-size="36" textLength="280" lengthAdjust="spacing">LUMBROVA</text>
      </g>
    </defs>

    <!-- Main pack face -->
    <use href="#pack-panel"/>
    <rect x="407" y="277" width="284" height="138" fill="url(#bedroom-tones)" role="img" aria-label="Replaceable lifestyle photo of a made bed with white pillows and a blue patterned throw"/>
    <rect class="photo-frame" x="406" y="276" width="286" height="140"/>

    <!-- Reduced layout preview -->
    <g transform="translate(830 97) scale(0.368 0.362) translate(-93 -117)">
      <use href="#pack-panel"/>
      <rect class="photo-slot-outline" x="406" y="276" width="286" height="140" vector-effect="non-scaling-stroke"/>
    </g>

    <!-- Preview callouts -->
    <polyline class="note-line" points="998,173 1100,173 1100,300 855,300"/>
    <polyline class="note-line" points="897,193 826,193 826,333 1088,333"/>
    <text class="note-text" x="855" y="297">REPLACEABLE PHOTO</text>
    <text class="note-text" x="855" y="332">YELLOW FABRIC TEXTURE</text>

    <!-- Footer -->
    <line class="footer-rule" x1="0" y1="738" x2="1200" y2="738"/>
    <text class="footer-caption" x="773" y="775">PROPOSAL FOR LUMBROVA PACK</text>
  </svg>
</div>
</body>
</html>
```